Mine Engineering Consultancy specializing in
* Pit optimization
* Mine Design
* Scheduling
* Mine Rehabilitation

Industry/Entity Type

Mining

Contact Information for Business Card

RVT Mining Pty Ltd
Derek Holloway
Director/Principle Mining Engineer
Mobile 0413582961
Email derek.holloway@rvtmining-example.com

```html
<!DOCTYPE html>
<html lang="en">
<head>
<meta charset="utf-8">
<title>RVT Mining Pty Ltd – Business Card</title>
<link rel="stylesheet" href="https://fonts.googleapis.com/css2?family=Roboto:wght@400&family=Tinos:wght@400&display=swap">
<style>
  :root {
    --brand-blue: #1a6fb8;
    --brand-blue-soft: #2a7cc2;
    --brand-blue-deep: #1767ad;
    --mark-blue: #3b88cb;
    --slate-grey: #6d6e70;
    --light-grey: #bcbdbf;
    --text-white: #ffffff;
  }
  html, body {
    margin: 0;
    padding: 0;
    overflow: hidden;
    background: #ffffff;
  }
  .card {
    position: relative;
    width: 1200px;
    height: 741px;
    overflow: hidden;
    background: var(--light-grey);
  }
  .card-panels {
    position: absolute;
    inset: 0;
    display: block;
  }
  .panel-slate { fill: var(--slate-grey); }
  .panel-light { fill: var(--light-grey); }
  .texture-stop-a { stop-color: var(--brand-blue-soft); }
  .texture-stop-b { stop-color: var(--brand-blue); }
  .texture-stop-c { stop-color: var(--brand-blue-deep); }

  .brand-mark {
    position: absolute;
    left: 90px;
    top: 170px;
    width: 300px;
    height: 300px;
    background: var(--mark-blue);
  }

  .services {
    position: absolute;
    inset: 0;
    margin: 0;
    padding: 0;
    list-style: none;
    font-family: "Roboto", Arial, sans-serif;
    font-size: 35px;
    line-height: 1;
    color: var(--text-white);
  }
  .service {
    position: absolute;
    white-space: nowrap;
  }
  .service::before {
    content: "•";
    font-size: 0.75em;
    margin-right: 0.35em;
    vertical-align: 0.12em;
  }
  .service--pit { left: 668px; top: 92px; }
  .service--design { left: 698px; top: 136px; }
  .service--scheduling { left: 735px; top: 188px; }
  .service--rehab { left: 772px; top: 241px; }

  .company-name {
    position: absolute;
    left: 406px;
    top: 492px;
    margin: 0;
    font-family: "Tinos", "Times New Roman", serif;
    font-weight: 400;
    font-size: 48px;
    line-height: 1;
    color: var(--text-white);
    white-space: nowrap;
  }
</style>
</head>
<body>
  <main class="card">
    <svg class="card-panels" width="1200" height="741" viewBox="0 0 1200 741" role="img" aria-label="Blue panel with fine diagonal line texture">
      <defs>
        <linearGradient id="blueTexture" x1="0" y1="0" x2="1" y2="1">
          <stop offset="0" class="texture-stop-a"/>
          <stop offset="0.55" class="texture-stop-b"/>
          <stop offset="1" class="texture-stop-c"/>
        </linearGradient>
      </defs>
      <polygon class="panel-light" points="900,481 1200,251 1200,741 573,741"/>
      <polygon class="panel-slate" points="578,0 1200,0 1200,251 900,481"/>
      <polygon fill="url(#blueTexture)" points="0,0 578,0 900,481 573,741 0,741"/>
    </svg>

    <div class="brand-mark" role="img" aria-label="Company monogram mark area"></div>

    <ul class="services">
      <li class="service service--pit">Pit Optimization</li>
      <li class="service service--design">Mine Design</li>
      <li class="service service--scheduling">Scheduling</li>
      <li class="service service--rehab">Mine Rehabilitation</li>
    </ul>

    <h1 class="company-name">RVT Mining Pty Ltd</h1>
  </main>
</body>
</html>
```